Brindle Pet Shop Homepage

We are a pet shop, we focus on dog food / cat food / rodents & bird food

Based on WooCommerce

It should be a simple but professional homepage with an informative start page. In the shop it should then be possible to shop for products/manufacturers etc. Navigation/Filter menu on the left would be ideal.

Next menus:
ABOUT US
CONTACT
DOG
CAT
HOLDER

My Account - Login
My Cart

Footer:
Conditions
payment options
social media

In addition to our logo, I have attached 2 example pages from another shop which we would use as a guideline.

Target Market(s)

pet store

Industry/Entity Type

Animal, Pet Shop

Coding

Coded - Design and coding required

Number of Pages Required

1 page

Font styles to use
Sans Serif

Colors
0054AA
0677BA
7BADD7
CADEEF
E8F1F8

Requirements
Must have
• Main Page, Contact, About Us, Shop, Check Out, Member Login, Mailchimp Marketing - We work with WooCommerce

```html
<!DOCTYPE html>
<html lang="en">
<head>
<meta charset="utf-8">
<title>Brindle Pet Shop – Premium Pet Food</title>
<link href="https://fonts.googleapis.com/css2?family=Poppins:wght@400;500;600;700;800&display=swap" rel="stylesheet">
<style>
:root{
  --navy:#0054AA;
  --blue:#0677BA;
  --mid:#7BADD7;
  --pale:#CADEEF;
  --mist:#E8F1F8;
  --ink:#333;
  --text:#555;
  --star:#F5A623;
  --dark:#4a4a4a;
  --white:#fff;
}
*{margin:0;padding:0;box-sizing:border-box}
html,body{width:1200px;height:3300px;overflow:hidden;background:var(--white)}
body{position:relative;font-family:"Poppins",sans-serif;color:var(--ink)}
.abs{position:absolute}
a{color:inherit;text-decoration:none}

/* header */
.brand{left:90px;top:42px;font-size:24px;font-weight:700;color:var(--navy);display:flex;align-items:center;gap:10px;line-height:1}
.brand-dot{width:34px;height:34px;border-radius:50%;background:var(--navy)}
.brand-sub{left:166px;top:86px;font-size:14px;letter-spacing:2px;color:#666;line-height:1}
.nav{left:584px;top:42px;display:flex;gap:34px;font-size:12px;font-weight:500;color:#555;align-items:center;line-height:14px}
.nav-tools{left:1046px;top:36px;display:flex;gap:20px}

/* hero */
.hero-circle{left:672px;top:92px;width:504px;height:504px;border-radius:50%;background:var(--mist)}
.hero-title{left:90px;top:252px;font-size:46px;line-height:53px;font-weight:800;color:var(--navy)}
.hero-text{left:90px;top:416px;width:400px;font-size:15px;line-height:21px;color:var(--text)}
.btn{display:flex;align-items:center;justify-content:center;gap:12px;width:150px;height:46px;border-radius:26px;font-size:13px;font-weight:700}
.btn-solid{background:var(--navy);color:var(--white);box-shadow:0 4px 0 var(--blue)}
.btn-line{border:2px solid var(--navy);color:#111}

/* categories */
.cat{top:685px;width:116px;text-align:center;font-size:15px;color:#333}
.cat-icon{width:116px;height:116px;border-radius:50%;margin-bottom:14px;display:flex;align-items:center;justify-content:center}
.cat-art{width:60px;height:60px;border-radius:10px}

/* about */
.h2{font-size:46px;font-weight:800;color:var(--navy);line-height:1.2}
.about-title{left:605px;top:984px}
.about-text{left:605px;top:1054px;width:490px;font-size:14.5px;line-height:22.3px;color:var(--text)}

/* products */
.products-title{left:0;width:1200px;top:1672px;text-align:center;color:var(--white)}
.card{top:1817px;width:248px;height:203px;background:var(--white);border-radius:8px;text-align:center;padding-top:110px;box-shadow:0 6px 16px rgba(0,0,0,.12)}
.card h3{font-size:17px;font-weight:700;color:#222;line-height:24px}
.stars{color:var(--star);font-size:14px;letter-spacing:4px;line-height:18px}
.price{font-size:20px;font-weight:700;color:#222;line-height:28px;margin-top:2px}
.pack{top:1754px;width:112px;height:156px;border-radius:6px}

/* reviews */
.review-title{left:0;width:1200px;top:2250px;text-align:center;font-size:56px}
.review{top:2355px;width:417px;height:222px;border-radius:34px;background:var(--white);box-shadow:0 8px 26px rgba(0,80,160,.10);padding:30px 34px}
.rev-head{display:flex;align-items:center;gap:18px}
.avatar{width:72px;height:72px;border-radius:50%;background:linear-gradient(135deg,#c9a78d,#6f5a4c)}
.rev-name{font-size:16px;font-weight:700;color:var(--blue)}
.rev-stars{color:var(--star);font-size:18px;letter-spacing:2px}
.quote{position:absolute;right:48px;top:14px;font-size:110px;font-weight:800;color:#eee;line-height:1}
.rev-text{margin-top:18px;font-size:14.5px;line-height:22.5px;color:var(--text)}
.dots{left:580px;top:2606px;display:flex;gap:8px}
.dots i{width:10px;height:10px;border-radius:50%;background:var(--pale)}
.dots i.on{background:var(--blue)}

/* newsletter */
.news{left:326px;top:2714px;width:686px;height:160px;border-radius:0 80px 80px 0;background:var(--blue)}
.news-title{left:415px;top:2762px;font-size:42px;font-weight:800;color:var(--white);line-height:1.1}
.news-sub{left:415px;top:2817px;font-size:16px;color:var(--white);line-height:1.2}
.news-input{left:668px;top:2777px;width:287px;height:45px;border-radius:24px;background:var(--white);display:flex;align-items:center;justify-content:space-between;padding:0 24px 0 26px;font-size:12px;color:#333}

/* footer */
.f-brand{left:116px;top:3074px;font-size:24px;font-weight:700;color:var(--white);display:flex;align-items:center;gap:10px;line-height:1}
.f-brand-sub{left:198px;top:3118px;font-size:15px;letter-spacing:2px;color:var(--white);line-height:1}
.f-col h4{font-size:17px;font-weight:700;color:var(--white);margin-bottom:10px;line-height:24px}
.f-col li{list-style:none;font-size:12.5px;color:#eee;line-height:25px}
.ico{display:inline-block;width:16px;color:var(--mid)}
.social{left:864px;top:3118px;display:flex;gap:12px;font-size:11px;color:var(--white);line-height:14px}
.social span{display:flex;align-items:center;gap:4px}
.social span::before{content:"";width:8px;height:8px;border-radius:50%;background:var(--white)}
.f-rule{left:90px;top:3240px;width:1020px;height:1px;background:#777}
.copy{left:92px;top:3260px;font-size:15px;font-weight:500;color:var(--white);line-height:20px}
.terms{left:778px;top:3260px;font-size:14px;color:var(--white);line-height:20px}
.pay{left:954px;top:3253px;display:flex;gap:9px}
.pay span{width:33px;height:33px;border-radius:50%;background:var(--white);color:var(--navy);font-size:7px;font-weight:700;display:flex;align-items:center;justify-content:center}
.chat{left:1114px;top:3206px;width:52px;height:52px;border-radius:50%;background:var(--blue);box-shadow:0 0 0 4px rgba(255,255,255,.4);display:flex;align-items:center;justify-content:center}
</style>
</head>
<body>

<!-- header -->
<div class="abs brand"><span class="brand-dot"></span>BRINDLE PET</div>
<div class="abs brand-sub">PREMIUM PET FOOD</div>
<nav class="abs nav">
  <svg width="16" height="14" viewBox="0 0 16 14"><path d="M8 0L0 7h2v7h4V9h4v5h4V7h2z" fill="var(--navy)"/></svg>
  <a>ABOUT US</a><a>CONTACT</a><a>DOG</a><a>CAT</a><a>HOLDER</a>
</nav>
<div class="abs nav-tools">
  <svg width="20" height="22" viewBox="0 0 20 22" fill="none" stroke="#555" stroke-width="1.5"><circle cx="10" cy="6" r="5"/><path d="M1 21c1-6 17-6 18 0"/></svg>
  <svg width="24" height="24" viewBox="0 0 24 24" fill="none" stroke="#555" stroke-width="1.5"><path d="M3 8h14v14H3z"/><path d="M6 8V5a4 4 0 018 0v3"/><circle cx="19" cy="5" r="5" fill="var(--navy)" stroke="none"/><text x="19" y="8" font-size="7" fill="#fff" stroke="none" text-anchor="middle" font-family="Poppins">0</text></svg>
</div>

<!-- hero -->
<div class="abs hero-circle"></div>
<svg class="abs" style="left:440px;top:110px" width="760" height="540" viewBox="0 0 760 540" role="img" aria-label="Dog, cat, budgie and ferret posed together beside scattered bird seed">
  <defs>
    <linearGradient id="petTone" x1="0" y1="0" x2="1" y2="1"><stop offset="0" stop-color="#6a5a4a"/><stop offset=".45" stop-color="#c7772e"/><stop offset=".75" stop-color="#e9d8bb"/><stop offset="1" stop-color="#d9c29a"/></linearGradient>
    <linearGradient id="seedTone" x1="0" y1="0" x2="1" y2="0"><stop offset="0" stop-color="#e6c27a" stop-opacity="0"/><stop offset=".5" stop-color="#d7a95a"/><stop offset="1" stop-color="#7fb54a"/></linearGradient>
  </defs>
  <path d="M240 120 C260 90 300 110 320 130 C380 40 470 10 570 30 C660 50 730 120 760 190 V440 C700 450 640 440 610 470 C560 530 470 520 400 480 C330 460 260 440 220 400 C190 360 200 280 210 240 Z" fill="url(#petTone)"/>
  <ellipse cx="140" cy="420" rx="120" ry="28" fill="url(#seedTone)"/>
</svg>
<h1 class="abs hero-title">Welcome to<br>Brindle Pet Premium<br>Pet Food</h1>
<p class="abs hero-text">We are a pet shop, we focus on dog food / cat food / rodents &amp; bird food.</p>
<a class="abs btn btn-solid" style="left:90px;top:472px">SHOP NOW <svg width="18" height="10" viewBox="0 0 18 10" fill="none" stroke="#fff" stroke-width="1.5"><path d="M0 5h16M12 1l4 4-4 4"/></svg></a>
<svg class="abs" style="left:0;top:544px" width="190" height="320" viewBox="0 0 190 320" role="img" aria-label="White bowl filled with dry kibble">
  <defs><radialGradient id="kib" cx=".4" cy=".4" r=".7"><stop offset="0" stop-color="#7a4e2a"/><stop offset="1" stop-color="#4a2d15"/></radialGradient></defs>
  <circle cx="24" cy="160" r="162" fill="#ececec"/>
  <circle cx="24" cy="160" r="150" fill="#fafafa"/>
  <circle cx="20" cy="150" r="124" fill="url(#kib)"/>
</svg>

<!-- categories -->
<div class="abs cat" style="left:357px"><div class="cat-icon" style="background:#FDF3CF"><div class="cat-art" role="img" aria-label="Dog food packs illustration" style="background:linear-gradient(135deg,#f7c948,#e66b3d)"></div></div>Dog food</div>
<div class="abs cat" style="left:480px"><div class="cat-icon" style="background:#FCE3E3"><div class="cat-art" role="img" aria-label="Cat food packs illustration" style="background:linear-gradient(135deg,#f47c7c,#4aa3df)"></div></div>Cat food</div>
<div class="abs cat" style="left:603px"><div class="cat-icon" style="background:#EFEFEF"><div class="cat-art" role="img" aria-label="Rodent food bag illustration" style="width:40px;background:linear-gradient(135deg,#e44b4b,#b52a2a)"></div></div>Rodents food</div>
<div class="abs cat" style="left:720px"><div class="cat-icon" style="background:var(--mist)"><div class="cat-art" role="img" aria-label="Bird on perch illustration" style="width:44px;background:linear-gradient(135deg,#f2b632,#e04a3b)"></div></div>Bird food</div>

<!-- about -->
<svg class="abs" style="left:0;top:864px" width="532" height="540" viewBox="0 0 532 540" role="img" aria-label="Dog and cat eating pet food from bowls on a wooden floor">
  <defs><linearGradient id="aboutTone" x1="0" y1="0" x2="1" y2="1"><stop offset="0" stop-color="#c98a4c"/><stop offset=".45" stop-color="#b8b4ad"/><stop offset="1" stop-color="#6c5a48"/></linearGradient></defs>
  <path d="M0 60 C120 20 260 -10 380 10 C470 25 530 100 530 220 C530 360 470 500 370 535 C300 555 240 500 170 440 C110 390 40 390 0 420 Z" fill="var(--mid)"/>
  <path d="M0 70 C120 35 250 15 360 30 C440 45 500 110 500 220 C500 350 450 480 360 520 C300 545 240 490 170 435 C110 385 40 385 0 410 Z" fill="url(#aboutTone)"/>
</svg>
<h2 class="abs h2 about-title">About Brindle Pet</h2>
<p class="abs about-text">Lorem Ipsum is simply dummy text of the printing and typesetting industry. Lorem Ipsum has been the industry's standard dummy text ever since the 1500s, when an unknown printer took a galley of type and scrambled it to make a type specimen book. It has survived not only five centuries, but also the leap into electronic typesetting, remaining essentially unchanged. It was popularised in the 1960s with the release of Letraset sheets containing .</p>
<a class="abs btn btn-line" style="left:605px;top:1230px">SHOP NOW <svg width="18" height="10" viewBox="0 0 18 10" fill="none" stroke="#111" stroke-width="1.5"><path d="M0 5h16M12 1l4 4-4 4"/></svg></a>

<!-- products -->
<svg class="abs" style="left:0;top:1280px" width="1200" height="870" viewBox="0 0 1200 870">
  <defs><linearGradient id="blueFade" x1="0" y1="0" x2="1" y2="0"><stop offset="0" stop-color="#1f6fb8"/><stop offset="1" stop-color="#0677BA"/></linearGradient></defs>
  <path d="M0 190 C120 150 230 200 330 260 C470 330 600 340 690 230 C790 110 880 40 1060 30 C1130 26 1170 28 1200 30 V870 H0Z" fill="url(#blueFade)"/>
  <path d="M0 200 C120 180 300 220 380 300 C400 380 380 470 300 500 C200 530 80 500 0 480Z" fill="#2a7fc4" opacity=".35"/>
</svg>
<svg class="abs" style="left:772px;top:1284px" width="336" height="160" viewBox="0 0 336 160" role="img" aria-label="White bowl of dry pet food">
  <path d="M0 0 H336 A168 160 0 0 1 0 0Z" fill="#f2f2f2"/>
  <path d="M20 0 H316 A148 130 0 0 1 20 0Z" fill="#a97c3c"/>
</svg>
<h2 class="abs h2 products-title">Our Products</h2>

<div class="abs card" style="left:89px"><h3>Products Heading</h3><div class="stars">★★★★★</div><div class="price">$52.00</div></div>
<div class="abs card" style="left:347px"><h3>Products Heading</h3><div class="stars">★★★★★</div><div class="price">$52.00</div></div>
<div class="abs card" style="left:605px"><h3>Products Heading</h3><div class="stars">★★★★★</div><div class="price">$52.00</div></div>
<div class="abs card" style="left:863px"><h3>Products Heading</h3><div class="stars">★★★★★</div><div class="price">$52.00</div></div>
<div class="abs pack" style="left:163px;background:linear-gradient(#4a3a30,#6a5040)" role="img" aria-label="Adult dog food bag"></div>
<div class="abs pack" style="left:409px;background:linear-gradient(#4a4aa0,#2f2f6e)" role="img" aria-label="Adult cat food bag"></div>
<div class="abs pack" style="left:678px;background:linear-gradient(#3aa0d8,#1a5f9e)" role="img" aria-label="Premium cat food box"></div>
<div class="abs pack" style="left:939px;border-radius:14px;background:linear-gradient(90deg,#c9d9ea,#fff,#7aa9d6)" role="img" aria-label="Dog food tin"></div>
<svg class="abs" style="left:72px;top:2038px" width="172" height="112" viewBox="0 0 172 112" role="img" aria-label="Rabbit peeking over the edge">
  <defs><linearGradient id="rab" x1="0" y1="0" x2="0" y2="1"><stop offset="0" stop-color="#e3a862"/><stop offset="1" stop-color="#b8702f"/></linearGradient></defs>
  <path d="M0 112 C10 60 40 30 86 26 C132 30 162 60 172 112Z" fill="url(#rab)"/>
</svg>

<!-- reviews -->
<h2 class="abs h2 review-title">Customer Review</h2>
<div class="abs review" style="left:93px"><span class="quote">“</span>
  <div class="rev-head"><div class="avatar" role="img" aria-label="Customer portrait"></div><div><div class="rev-name">Marlon Okafor</div><div class="rev-stars">★★★★<span style="color:#ddd">★</span></div></div></div>
  <p class="rev-text">It is a long established fact that a reader will be distracted by the readable content of a page when looking at its layout. It is a long...</p></div>
<div class="abs review" style="left:539px"><span class="quote">“</span>
  <div class="rev-head"><div class="avatar" role="img" aria-label="Customer portrait"></div><div><div class="rev-name">Daniel Chow</div><div class="rev-stars">★★★★<span style="color:#ddd">★</span></div></div></div>
  <p class="rev-text">It is a long established fact that a reader will be distracted by the readable content of a page when looking at its layout. It is a long...</p></div>
<div class="abs review" style="left:985px"><span class="quote">“</span>
  <div class="rev-head"><div class="avatar" role="img" aria-label="Customer portrait"></div><div><div class="rev-name">Ravi Stone</div><div class="rev-stars">★★★★<span style="color:#ddd">★</span></div></div></div>
  <p class="rev-text">It is a long established fact that a reader will be distracted by the readable content of a page when looking at its layout. It is a long...</p></div>
<div class="abs dots"><i></i><i class="on"></i><i></i></div>

<!-- newsletter -->
<svg class="abs" style="left:0;top:2780px" width="1200" height="520" viewBox="0 0 1200 520"><path d="M0 60 C300 -20 700 40 900 70 C1050 90 1150 30 1200 10 V520 H0Z" fill="var(--dark)"/></svg>
<div class="abs news"></div>
<svg class="abs" style="left:134px;top:2668px" width="258" height="252" viewBox="0 0 258 252" role="img" aria-label="Puppy and kitten sitting behind a bowl of kibble">
  <defs><linearGradient id="pup" x1="0" y1="0" x2="1" y2="1"><stop offset="0" stop-color="#e0b07a"/><stop offset=".5" stop-color="#c9864a"/><stop offset="1" stop-color="#f3e6d6"/></linearGradient></defs>
  <path d="M20 90 C40 70 70 80 90 90 C110 30 170 0 230 20 C250 60 258 140 240 200 L30 200 C10 160 5 120 20 90Z" fill="url(#pup)"/>
  <path d="M30 200 C30 170 50 165 70 165 L210 165 C230 165 240 175 240 200Z" fill="#c8903e"/>
  <path d="M30 200 H240 L220 245 H50Z" fill="#cfd3d6"/>
</svg>
<div class="abs news-title">Newsletter</div>
<div class="abs news-sub">Subscribe to our newsletter</div>
<div class="abs news-input">Email Address <svg width="14" height="12" viewBox="0 0 14 12"><path d="M0 5L14 0 10 12 7 7z" fill="var(--blue)"/></svg></div>

<!-- footer -->
<div class="abs f-brand"><span class="brand-dot" style="background:var(--white)"></span>BRINDLE PET</div>
<div class="abs f-brand-sub">PREMIUM PET FOOD</div>
<div class="abs f-col" style="left:472px;top:2983px"><h4>Useful Links</h4><ul><li>About Us</li><li>Contact</li><li>Dog</li><li>Cat</li><li>Holder</li></ul></div>
<div class="abs f-col" style="left:653px;top:2983px"><h4>Our Products</h4><ul><li>Dog food</li><li>Cat food</li><li>Rodents Food</li><li>Bird food</li></ul></div>
<div class="abs f-col" style="left:864px;top:2983px"><h4>Contact Us</h4><ul style="line-height:21px">
  <li><span class="ico">◷</span>9am - 6pm Mon - Fri (ET)</li><li style="padding-left:16px">10am - 3pm Sat (ET)</li>
  <li><span class="ico">✆</span>(555) 014-2290</li><li><span class="ico">✉</span>hello@brindlepet.shop</li></ul></div>
<div class="abs social"><span>Pawbook</span><span>Chirper</span><span>Snapgram</span><span>Vidtube</span></div>
<div class="abs f-rule"></div>
<div class="abs copy">©Copyright 2023 | All Rights Reserved</div>
<div class="abs terms">Terms &amp; Conditions</div>
<div class="abs pay"><span>Orbit</span><span>Amerpay</span><span>Veza</span><span>Jecard</span></div>
<div class="abs chat"><svg width="22" height="20" viewBox="0 0 22 20"><path d="M11 1C5 1 1 5 1 9c0 2.5 1.4 4.6 3.6 6L3 19l5-2.6c1 .3 2 .4 3 .4 6 0 10-4 10-8S17 1 11 1z" fill="#fff"/></svg></div>

</body>
</html>
```